Korvel Bloom , Australian natural body care needs a new product label.

I have just had a logo designed by artflockr and now want this logo added to a product label design. The product is a cleansing, moisturising hand scrub with only natural ingredients and anti microbial essential oils. I have made this product for over 15 years and it needs a new more appropriate image. It was previously called velvet tonic and came in a tube. the new packaging is a white pump pack container. Dimensions for the label are 185mm wide and 80mm high, I have attached a sheet with all of the information required on the label.
Updates

Target Market(s)

anyone with dry skin

Industry/Entity Type

Cosmetics

Requirements
Must have
• professional and upmarket appearance. Be creative and surprise me your take on how this label should look.
Nice to have
• Natural colours, the attached logo should be changed in colour to match the label.

```html
<!DOCTYPE html>
<html lang="en">
<head>
<meta charset="utf-8">
<title>Korvel Bloom Hand Scrub Label</title>
<link href="https://fonts.googleapis.com/css2?family=Archivo+Black&family=Open+Sans:ital,wght@1,700&family=Oswald:wght@300&family=Quicksand:wght@500&display=swap" rel="stylesheet">
<style>
  :root {
    --backdrop: #dcdcdc;
    --label: #ffffff;
    --magenta: #cf5fae;
    --magenta-light: #e98fd0;
    --magenta-dark: #6a2454;
    --blue: #3562a8;
    --ink: #1f1a17;
    --text: #333333;
    --rose: #c8221b;
    --rose-light: #e85a44;
    --flourish: #c9c9c9;
  }
  * { margin: 0; padding: 0; box-sizing: border-box; }
  html, body { width: 1200px; height: 1052px; overflow: hidden; }
  body { background: var(--backdrop); position: relative; font-family: "Quicksand", sans-serif; }

  .label {
    position: absolute; left: 300px; top: 106px; width: 602px; height: 840px;
    background: var(--label);
  }
  .label > * { position: absolute; }

  .top-band {
    left: 0; top: 0; width: 100%; height: 58px;
    background: linear-gradient(90deg, var(--magenta) 0%, var(--magenta) 30%, var(--magenta-light) 38%, var(--magenta) 55%, var(--magenta-dark) 100%);
  }

  .brand-mark {
    left: 271px; top: 110px; width: 60px; height: 60px; border-radius: 50%;
    background: var(--magenta);
  }
  .brand-name {
    left: 0; width: 100%; top: 196px; text-align: center;
    font-weight: 500; font-size: 46px; color: var(--ink); line-height: 1;
  }

  .product-title {
    left: 0; width: 100%; top: 300px; text-align: center;
    font-family: "Archivo Black", sans-serif; font-size: 52px; letter-spacing: 1px;
    color: var(--ink); line-height: 1; font-weight: 400;
  }
  .product-benefit {
    left: 105px; top: 367px; width: 395px; height: 53px;
    background: var(--blue); color: #fff;
    font-family: "Open Sans", sans-serif; font-style: italic; font-weight: 700; font-size: 31px;
    display: flex; align-items: center; justify-content: center; letter-spacing: -0.5px;
  }
  .claims {
    left: 0; width: 100%; top: 448px; text-align: center;
    font-size: 24px; line-height: 33px; color: var(--text);
  }

  .divider {
    left: 226px; top: 544px; width: 150px; height: 20px;
    background: linear-gradient(90deg, transparent, var(--flourish) 20%, var(--flourish) 80%, transparent);
    border-radius: 10px;
  }

  .natural-seal {
    left: 48px; top: 522px; width: 84px; height: 100px; border-radius: 50%;
    background: var(--blue); color: #fff; text-align: center;
    display: flex; flex-direction: column; align-items: center; justify-content: center;
    font-family: "Oswald", sans-serif; font-weight: 300; line-height: 1;
  }
  .natural-seal .seal-percent { font-size: 12px; margin-bottom: 4px; }
  .natural-seal .seal-word { font-size: 22px; letter-spacing: 0.5px; }

  .ingredient-note {
    left: 17px; top: 645px; width: 281px; height: 95px;
    background: var(--blue); color: #fff;
    font-size: 23px; line-height: 31px; text-align: center;
    display: flex; align-items: center; justify-content: center;
  }

  .rosehip-photo {
    left: 320px; top: 565px; width: 270px; height: 175px;
    background: radial-gradient(ellipse at 55% 50%, var(--rose-light) 0%, var(--rose) 50%, rgba(200,34,27,0.4) 68%, rgba(255,255,255,0) 78%);
  }

  .net-weight {
    left: 17px; top: 775px; width: 110px; height: 62px;
    background: var(--magenta); color: var(--magenta-dark);
    font-size: 18px; display: flex; align-items: center; justify-content: center;
  }
  .origin {
    left: 365px; top: 798px; width: 210px; text-align: right;
    font-size: 25px; color: var(--ink);
  }
</style>
</head>
<body>
  <main class="label">
    <div class="top-band"></div>

    <div class="brand-mark"></div>
    <div class="brand-name">Korvel Bloom</div>

    <h1 class="product-title">HAND SCRUB</h1>
    <div class="product-benefit">Cleansing &amp; Moisturising</div>
    <p class="claims">Dry &amp; Damaged Hand Repair<br>Immediate results</p>

    <div class="divider" role="img" aria-label="Decorative flourish divider"></div>

    <div class="natural-seal">
      <span class="seal-percent">100%</span>
      <span class="seal-word">NATURAL</span>
    </div>

    <p class="ingredient-note">Ultra-moisturising with<br>Rosehip &amp; essential oil</p>

    <div class="rosehip-photo" role="img" aria-label="Photo of fresh red rosehip berries on a stem"></div>

    <div class="net-weight">250gm</div>
    <p class="origin">Made in Australia</p>
  </main>
</body>
</html>
```